Email Notification & Marketing Templates

I want to start with something like a newsletter or informational email, but i need Top Tips to Detect Phishing Scams. Something that i can send to users so they can follow it when receiving or exchanging emails. I will also need promotional items for my company that i can send to customers as well. It can be based on on our website PLVORIX.COM

Will also need:
newsletters
announcements
marketing emails
alerts
security notifications

Examples:Items such as Security Awareness Poster Series
Phishing Awareness
Password Security
Email Attachments
QR Code scams
Public WiFi safety

```html
<!DOCTYPE html>
<html lang="en">
<head>
<meta charset="utf-8">
<title>Strengthen Your Passwords Today – Plvorix</title>
<link rel="stylesheet" href="https://fonts.googleapis.com/css2?family=Lexend:wght@300;400;500;600;700&display=swap">
<style>
  :root {
    --page-bg: #f4f5f4;
    --card-bg: #ffffff;
    --brand-green: #2f8a1e;
    --brand-green-dark: #1f5e17;
    --ink: #1c3a1f;
    --ink-soft: #2b2b2b;
    --weak-red: #d63a3a;
    --strong-green: #2e8b22;
    --panel-tint: #eef6ee;
    --line: #dfe6df;
    --hero-a: #e6f6f1;
    --hero-b: #5cc2a3;
    --hero-c: #0d4a4a;
  }
  * { box-sizing: border-box; margin: 0; padding: 0; }
  html, body { width: 800px; height: 1200px; overflow: hidden; }
  body {
    background: var(--page-bg);
    font-family: "Lexend", sans-serif;
    color: var(--ink-soft);
    position: relative;
  }
  .email {
    position: absolute; left: 80px; top: 64px;
    width: 640px; height: 1081px;
    background: var(--card-bg);
    box-shadow: 0 1px 6px rgba(0,0,0,.06);
  }
  .brand {
    position: absolute; left: 34px; top: 26px;
    display: flex; align-items: center; gap: 10px;
  }
  .brand-mark { width: 22px; height: 22px; background: var(--brand-green); }
  .brand-name {
    font-size: 40px; font-weight: 700; color: var(--brand-green);
    letter-spacing: -0.5px; line-height: 1;
  }
  .hero {
    position: absolute; left: 0; top: 106px; width: 640px; height: 227px;
    overflow: hidden;
  }
  .hero-art {
    position: absolute; inset: 0;
    background:
      radial-gradient(circle at 77% 50%, rgba(110,230,170,.75) 0 70px, rgba(40,150,120,.4) 110px, transparent 170px),
      linear-gradient(100deg, var(--hero-a) 0%, #c6ece0 35%, var(--hero-b) 62%, var(--hero-c) 100%);
  }
  .hero-title {
    position: absolute; left: 29px; top: 48px;
    font-size: 40px; font-weight: 600; line-height: 1.05;
    color: var(--brand-green-dark); letter-spacing: -0.4px;
  }
  .hero-title span { display: block; color: var(--brand-green); }
  .compare {
    position: absolute; left: 18px; top: 362px; width: 604px; height: 281px;
    background: linear-gradient(180deg, #f3f7f3, var(--panel-tint) 60%, #f6faf6);
  }
  .compare-title {
    position: absolute; top: 12px; width: 100%; text-align: center;
    font-size: 27px; font-weight: 500; color: var(--ink);
  }
  .compare-title em { font-style: normal; color: var(--brand-green); }
  .divider-v { position: absolute; left: 370px; top: 68px; width: 1px; height: 182px; background: #cfe0cf; }
  .vs {
    position: absolute; left: 346px; top: 181px; width: 48px; height: 48px;
    border-radius: 50%; background: radial-gradient(circle at 40% 35%, #3f9a4a, #17602a);
    color: #fff; font-weight: 600; font-size: 19px;
    display: flex; align-items: center; justify-content: center;
    box-shadow: 0 2px 4px rgba(0,0,0,.2);
  }
  .pw-card {
    position: absolute; top: 74px; height: 173px; border-radius: 10px;
    border: 3px solid #fff; box-shadow: 0 2px 6px rgba(0,0,0,.12);
    padding: 30px 14px 0 19px;
  }
  .pw-card.weak { left: 18px; width: 229px; background: linear-gradient(#f7f7f8, #e2e3e6); }
  .pw-card.strong { left: 332px; width: 254px; background: linear-gradient(#f6fbf4, #d9efd6); }
  .pw-tab {
    position: absolute; top: -14px; height: 30px; border-radius: 6px;
    color: #fff; font-size: 17px; font-weight: 500;
    display: flex; align-items: center; justify-content: center; gap: 8px;
    box-shadow: 0 2px 3px rgba(0,0,0,.15);
  }
  .weak .pw-tab { left: 15px; right: 20px; background: var(--weak-red); }
  .strong .pw-tab { left: 14px; right: 14px; background: var(--strong-green); }
  .pw-sample {
    display: flex; align-items: center; gap: 8px;
    font-size: 16.5px; font-weight: 500; color: #1c1c1c;
    padding-bottom: 12px; border-bottom: 1px dashed #c6c8c6; margin-bottom: 9px;
  }
  .pw-sample svg { flex: none; }
  .pw-points { list-style: none; font-size: 13.5px; line-height: 22.5px; color: #2c2c2c; }
  .pw-points li { position: relative; padding-left: 18px; }
  .pw-points li::before {
    content: ""; position: absolute; left: 4px; top: 9px;
    width: 5px; height: 5px; border-radius: 50%;
  }
  .weak .pw-points li::before { background: var(--weak-red); }
  .strong .pw-points li::before { background: var(--brand-green-dark); }
  .tips-title {
    position: absolute; top: 666px; width: 100%; text-align: center;
    font-size: 25px; font-weight: 500; color: var(--ink);
  }
  .tips {
    position: absolute; left: 25px; top: 716px; width: 589px; height: 226px;
    background: #fff; border-radius: 8px; box-shadow: 0 1px 6px rgba(0,0,0,.1);
    list-style: none;
  }
  .tip { position: absolute; left: 0; right: 0; display: flex; }
  .tip-icon {
    position: absolute; left: 23px; width: 46px; height: 46px; border-radius: 50%;
    background: radial-gradient(circle at 40% 35%, #4fae3c, #1e6d1a);
    display: flex; align-items: center; justify-content: center;
    box-shadow: 0 2px 3px rgba(0,0,0,.2);
  }
  .tip-text { position: absolute; left: 84px; right: 20px; font-size: 16.5px; line-height: 27px; color: #333; }
  .tip-text b { font-weight: 600; color: var(--ink); }
  .tip + .tip::before {
    content: ""; position: absolute; left: 84px; right: 20px; top: -8px;
    height: 1px; background: var(--line);
  }
  .tip-1 { top: 20px; } .tip-1 .tip-icon { top: 6px; }
  .tip-2 { top: 78px; } .tip-2 .tip-icon { top: 14px; }
  .tip-3 { top: 144px; } .tip-3 .tip-icon { top: 16px; }
  .cta {
    position: absolute; left: 125px; top: 983px; width: 383px; height: 58px;
    border-radius: 29px; background: linear-gradient(#5bb32f, #2b7f1b 70%, #23701a);
    color: #fff; font-size: 27px; font-weight: 500; text-decoration: none;
    display: flex; align-items: center; justify-content: center;
    box-shadow: 0 3px 5px rgba(0,0,0,.2);
  }
</style>
</head>
<body>
  <main class="email">
    <header class="brand">
      <span class="brand-mark"></span>
      <span class="brand-name">PLVORIX</span>
    </header>

    <section class="hero">
      <div class="hero-art" role="img" aria-label="Glowing green security shield with a padlock over a teal digital circuit background"></div>
      <h1 class="hero-title">Strengthen Your <span>Passwords Today</span></h1>
    </section>

    <section class="compare">
      <h2 class="compare-title">Is Your Password <em>Strong?</em></h2>
      <div class="divider-v"></div>

      <article class="pw-card weak">
        <div class="pw-tab">Weak Password</div>
        <p class="pw-sample">
          <svg width="20" height="20" viewBox="0 0 20 20"><circle cx="10" cy="10" r="10" fill="#d63a3a"/><rect x="8.7" y="4" width="2.6" height="8" rx="1.2" fill="#fff"/><circle cx="10" cy="15" r="1.5" fill="#fff"/></svg>
          password123
        </p>
        <ul class="pw-points">
          <li>Too short</li>
          <li>No special characters</li>
          <li>Common or predictable</li>
        </ul>
      </article>

      <div class="vs">VS</div>

      <article class="pw-card strong">
        <div class="pw-tab">Strong Password
          <svg width="16" height="14" viewBox="0 0 16 14"><path d="M1.5 7.5l4.5 4.5 8.5-10" fill="none" stroke="#fff" stroke-width="2.6" stroke-linecap="round" stroke-linejoin="round"/></svg>
        </div>
        <p class="pw-sample">
          <svg width="20" height="20" viewBox="0 0 20 20"><circle cx="10" cy="10" r="10" fill="#1f6e1f"/><path d="M5.5 10.3l3 3 6-6.5" fill="none" stroke="#fff" stroke-width="2.2" stroke-linecap="round" stroke-linejoin="round"/></svg>
          V3rY$3cur3Pl4c3!9
        </p>
        <ul class="pw-points">
          <li>12+ characters</li>
          <li>Mix of symbols, numbers, uppercase &amp; lowercase</li>
          <li>Unique and unpredictable</li>
        </ul>
      </article>
    </section>

    <h2 class="tips-title">Top Tips for a Secure Password</h2>
    <ul class="tips">
      <li class="tip tip-1">
        <span class="tip-icon"><svg width="26" height="28" viewBox="0 0 26 28"><path d="M13 2l10 4v7c0 6.5-4.3 11-10 13C7.3 24 3 19.5 3 13V6z" fill="none" stroke="#fff" stroke-width="2.2" stroke-linejoin="round"/><path d="M8.5 14l3.2 3.2 6-6.5" fill="none" stroke="#fff" stroke-width="2.2" stroke-linecap="round" stroke-linejoin="round"/></svg></span>
        <p class="tip-text"><b>Go Long:</b> Use at least 12 characters.</p>
      </li>
      <li class="tip tip-2">
        <span class="tip-icon"><svg width="26" height="26" viewBox="0 0 26 26"><g stroke="#fff" stroke-width="3" stroke-linecap="round"><path d="M13 3v20M4.3 8l17.4 10M4.3 18l17.4-10"/></g></svg></span>
        <p class="tip-text"><b>Add Symbols:</b> Include symbols, numbers, and uppercase &amp; lowercase letters.</p>
      </li>
      <li class="tip tip-3">
        <span class="tip-icon"><svg width="26" height="28" viewBox="0 0 26 28"><path d="M13 2l10 4v7c0 6.5-4.3 11-10 13C7.3 24 3 19.5 3 13V6z" fill="none" stroke="#fff" stroke-width="2.2" stroke-linejoin="round"/><circle cx="15.5" cy="15" r="5" fill="#fff"/><rect x="14.3" y="13" width="2.4" height="4" rx="1" fill="#2b7f1b"/></svg></span>
        <p class="tip-text"><b>Enable 2FA:</b> Turn on Two-Factor Authentication for added security.</p>
      </li>
    </ul>

    <a class="cta" href="#">Secure Your Account</a>
  </main>
</body>
</html>
```